New Brochure for existing Virtual Reality Amusement Arena

I need a two sided half page brochure for my arcade. it needs to say what we do and what we have to offer. It basically needs to be a paper copy of all the information thats on my website www.kavimo-nix.com
Please check that as it is very informative!
Industry/Entity Type
Entertainment
Colors
Designer to choose colors to be used in the design.
Requirements
Must have
- Color. I have uploaded an old brochure I had made, but now we have a new company and new logo, please make it similar to that. Please pull all pics from my website www.kavimo-nix.com
Should not have
- useless information

```html
<!DOCTYPE html>
<html lang="en">
<head>
<meta charset="utf-8">
<title>Kavimo-Nix Brochure</title>
<link rel="stylesheet" href="https://fonts.googleapis.com/css2?family=Archivo+Black&family=Montserrat:wght@400;500;600;700&display=swap">
<style>
:root{
  --bg:#c7c6c9;
  --ink:#141315;
  --ink-2:#1d1b1e;
  --wine:#5e1620;
  --red:#a8222e;
  --red-bright:#c42733;
  --violet:#6d4d9a;
  --blue:#3c4fa8;
  --white:#ffffff;
  --muted:#b9b5ba;
  --line:rgba(255,255,255,.35);
}
*{box-sizing:border-box;margin:0;padding:0}
html,body{width:918px;height:1200px;overflow:hidden;background:var(--bg)}
body{font-family:"Montserrat",sans-serif;color:var(--white);position:relative}
.page{position:absolute;top:308px;width:420px;height:584px;overflow:hidden;
  background:linear-gradient(180deg,var(--wine) 0%,#2a1519 30%,var(--ink-2) 55%,var(--ink) 100%);
  box-shadow:0 6px 18px rgba(0,0,0,.35)}
.page--front{left:26px}
.page--back{left:472px}

/* brand lockup */
.brand{display:flex;align-items:center;gap:8px;font-weight:700;letter-spacing:.06em;color:var(--white)}
.brand__dot{width:18px;height:18px;border-radius:50%;background:var(--white);flex:none}

/* front */
.hero-photo{position:absolute;left:0;top:0;width:420px;height:420px;
  background:radial-gradient(ellipse at 70% 35%,rgba(150,110,210,.75),transparent 55%),
  linear-gradient(180deg,rgba(94,22,32,.9) 0%,rgba(90,70,150,.7) 40%,rgba(40,35,70,.55) 70%,rgba(20,19,21,0) 100%)}
.page--front .brand{position:absolute;right:28px;top:48px;font-size:15px}
.headline{position:absolute;left:22px;top:220px;font-family:"Archivo Black",sans-serif;font-size:30px;line-height:33px;text-transform:uppercase}
.headline__accent{color:var(--red-bright);display:block}
.tagline{position:absolute;left:22px;top:388px;font-size:9.5px;line-height:13px;color:#e6e3e7}
.hex{position:absolute;width:94px;height:100px;clip-path:polygon(50% 0,100% 25%,100% 75%,50% 100%,0 75%,0 25%)}
.hex--one{left:22px;top:438px;background:linear-gradient(135deg,#3345b8,#8a2e5a 55%,#1b1d4a)}
.hex--two{left:120px;top:458px;background:linear-gradient(160deg,#3a6fb0,#1f3a66 60%,#0e1a30)}
.url-band{position:absolute;left:0;bottom:0;width:420px;height:26px}
.url-band__text{position:absolute;right:16px;bottom:6px;font-size:10.5px;font-weight:500;letter-spacing:.02em}

/* back */
.page--back .brand{position:absolute;left:0;right:0;top:36px;justify-content:center;font-size:22px}
.page--back .brand__dot{width:28px;height:28px}
.section-title{position:absolute;left:90px;right:90px;top:80px;height:28px;display:flex;align-items:center}
.section-title::before,.section-title::after{content:"";flex:1;height:1px;background:var(--line)}
.section-title span{border:1.5px solid var(--white);border-radius:14px;padding:4px 14px;font-size:13px;font-weight:500;letter-spacing:.04em;white-space:nowrap}
.offers{position:absolute;left:52px;top:123px;width:314px;display:grid;grid-template-columns:153px 153px;gap:8px}
.offer{border:1px solid rgba(255,255,255,.3);border-radius:3px;height:160px;padding:12px 8px 8px;text-align:center;background:rgba(0,0,0,.15)}
.offer__icon{display:block;margin:0 auto 6px;height:34px}
.offer__title{font-size:10.5px;font-weight:600;letter-spacing:.02em;margin-bottom:8px}
.offer__text{font-size:6.4px;line-height:8.8px;color:#d6d3d7}
.owner{position:absolute;right:18px;top:486px;text-align:right}
.owner__label{font-size:9px;color:#d8d5d9;letter-spacing:.02em}
.owner__name{font-size:14px;font-weight:600;color:var(--red);text-transform:uppercase;margin-top:1px;padding-bottom:6px;border-bottom:1px solid rgba(168,34,46,.6);margin-bottom:6px}
.contact{list-style:none;font-size:8.6px;line-height:12.6px}
.contact li{display:flex;justify-content:flex-end;align-items:center;gap:5px}
.contact svg{width:8px;height:8px;flex:none}
</style>
</head>
<body>

<section class="page page--front" aria-label="Front page">
  <div class="hero-photo" role="img" aria-label="Photo of a virtual reality motion rig in a dim lounge lit in purple and blue"></div>
  <div class="brand"><span class="brand__dot"></span>KAVIMO-NIX</div>
  <h1 class="headline">Gaming<br>Like<span class="headline__accent">You’ve<br>Never<br>Seen</span></h1>
  <p class="tagline">A virtual reality amusement<br>park and video game lounge.</p>
  <div class="hex hex--one" role="img" aria-label="Photo of a player in a VR headset aiming in a motion rig"></div>
  <div class="hex hex--two" role="img" aria-label="Photo of a player in a VR headset and haptic vest"></div>
  <div class="url-band">
    <svg width="420" height="26" viewBox="0 0 420 26"><polygon points="270,0 420,0 420,26 250,26" fill="var(--wine)"/><rect x="0" y="23" width="420" height="3" fill="var(--wine)"/></svg>
    <span class="url-band__text">www.kavimo-nix.com</span>
  </div>
</section>

<section class="page page--back" aria-label="Back page">
  <div class="brand"><span class="brand__dot"></span>KAVIMO-NIX</div>
  <h2 class="section-title"><span>WHAT WE DO</span></h2>

  <div class="offers">
    <article class="offer">
      <svg class="offer__icon" viewBox="0 0 34 34" fill="none" stroke="var(--red)" stroke-width="1.6" stroke-linecap="round" stroke-linejoin="round"><circle cx="21" cy="6" r="3"/><path d="M19 11l-5 8 6 4-3 9M14 19l-7 3M19 11l5 5 5-1"/></svg>
      <h3 class="offer__title">IMMERSIVE VR</h3>
      <p class="offer__text">Powered by Stridelab, we have Bayview’s only fully immersive VR. These machines allow you to walk inside virtual reality. When you walk in real life, you walk in the game. The game selection is limited, but the experience is the most unique.</p>
    </article>
    <article class="offer">
      <svg class="offer__icon" viewBox="0 0 34 34" fill="none" stroke="var(--red)" stroke-width="1.6" stroke-linecap="round" stroke-linejoin="round"><path d="M17 2v10"/><rect x="4" y="12" width="26" height="16" rx="4"/><path d="M11 17v6M8 20h6"/><circle cx="22" cy="19" r="1"/><circle cx="25" cy="22" r="1"/></svg>
      <h3 class="offer__title">HALO PLAY</h3>
      <p class="offer__text">The gold standard in VR made by Halcyon. This has the best selection of games, and the most fun in our opinion. A great variety of multiplayer and single player games, for kids and adults, this is fun for all ages. We currently have two of these stations allowing two to link up and play together or by yourself.</p>
    </article>
    <article class="offer">
      <svg class="offer__icon" viewBox="0 0 34 34" fill="none" stroke="var(--red)" stroke-width="1.6" stroke-linecap="round" stroke-linejoin="round"><path d="M6 26V18a11 11 0 0 1 22 0v8H6z"/><rect x="3" y="14" width="11" height="9" rx="2"/></svg>
      <h3 class="offer__title">SEATED VR</h3>
      <p class="offer__text">For both the relaxed individual who isn’t familiar with video games, and the in-depth everyday gamer, these stations are great for both. We have selections that allow you to experience a different world with hardly any effort, and the advanced campaign based games that come with a console controller. This is a terrific station for gamers and non-gamers alike.</p>
    </article>
    <article class="offer">
      <svg class="offer__icon" viewBox="0 0 34 34" fill="none" stroke="var(--red)" stroke-width="1.6" stroke-linecap="round" stroke-linejoin="round"><circle cx="20" cy="5" r="3"/><path d="M18 10l-4 9 6 4-2 9M14 19l-6 2M18 10l6 5 4-2"/><rect x="20" y="11" width="6" height="7" rx="1"/></svg>
      <h3 class="offer__title">FREE ROAM VR</h3>
      <p class="offer__text">Completely wireless, walk and move freely in your space with a top of the line Norvek laptop strapped to your back. This is the way virtual reality was meant to be played, with no restrictions. Feel and move like a soldier shooting a rifle, jump off walls and wield swords like a ninja, this is our most realistic experience yet.</p>
    </article>
  </div>

  <div class="owner">
    <p class="owner__label">OWNER OPERATED BY</p>
    <p class="owner__name">Dana Whitfield</p>
    <ul class="contact">
      <li>2715 W Harbor Rd, Bayview FL 33990<svg viewBox="0 0 8 8"><circle cx="4" cy="4" r="4" fill="var(--red)"/><circle cx="4" cy="3.4" r="1.2" fill="var(--ink)"/></svg></li>
      <li>Office: 555.204.3318<svg viewBox="0 0 8 8"><circle cx="4" cy="4" r="4" fill="var(--red)"/><path d="M2.6 2.4l1 1-.5.6 1 1 .6-.5 1 1-.8.8C3.8 6 2 4.2 1.9 3.2z" fill="var(--ink)"/></svg></li>
      <li>Write us: dana@kavimo-nix.com<svg viewBox="0 0 8 8"><circle cx="4" cy="4" r="4" fill="var(--red)"/><rect x="2" y="2.8" width="4" height="2.6" fill="none" stroke="var(--ink)" stroke-width=".7"/></svg></li>
      <li>Check us out: www.brightlanestudio.com<svg viewBox="0 0 8 8"><circle cx="4" cy="4" r="4" fill="var(--red)"/><circle cx="4" cy="4" r="1.8" fill="none" stroke="var(--ink)" stroke-width=".7"/></svg></li>
    </ul>
  </div>
  <svg style="position:absolute;left:0;bottom:0" width="420" height="3"><rect width="420" height="3" fill="var(--wine)"/></svg>
</section>

</body>
</html>
```